The Pledge a non-fiction book on mindfulness COVER design needed

A non-fiction book about active mindfulness.
The Pledge includes 21 different daily 'dares' which are action based activities to generate positive mindfulness - to become more contented with life.
Based on the teeaching of the New Thought movements of the early 20th century, think The Lantern, Plan and Become Bold.
The book is positive and uplifting. It fits into the self-help / spiritual / health segments. It skews female 40 to 50 year olds.
Think fresh colours like a bold orange or bright green.
What needs to be on the cover:
TITLE: The Pledge
AUTHOR: Marcus Pellworth
BLURB: Get clarity, focus, and a new zest for life by following The Pledge for just 21 days.
Target Market(s)
Women 40-50 english speaking
Industry/Entity Type
Self-help / Health

```html
<!DOCTYPE html>
<html lang="en">
<head>
<meta charset="utf-8">
<title>The Pledge — Book Cover</title>
<link rel="stylesheet" href="https://fonts.googleapis.com/css2?family=Montserrat:wght@600&family=EB+Garamond&family=Oswald:wght@400&display=swap">
<style>
  :root {
    --stage: #e4e4e4;
    --paper: #f7f7f7;
    --teal: #68c3c8;
    --orange: #d85528;
    --orange-deep: #d24a1c;
    --amber: #e0832e;
    --author: #e07b2a;
    --white: #ffffff;
  }
  html, body {
    margin: 0;
    padding: 0;
    width: 1200px;
    height: 960px;
    overflow: hidden;
    background: var(--stage);
  }
  .canvas {
    position: relative;
    width: 1200px;
    height: 960px;
    background: var(--stage);
  }
  .cover {
    position: absolute;
    left: 330px;
    top: 85px;
    width: 540px;
    height: 790px;
    background: var(--paper);
    overflow: hidden;
    box-shadow: 0 10px 30px rgba(0,0,0,0.12);
  }
  .cover-title-top {
    position: absolute;
    top: 60px;
    left: 0;
    width: 100%;
    margin: 0;
    text-align: center;
    font-family: "Montserrat", sans-serif;
    font-weight: 600;
    font-size: 62px;
    letter-spacing: 0.42em;
    text-indent: 0.42em;
    color: var(--teal);
    line-height: 1;
  }
  .cover-author {
    position: absolute;
    top: 200px;
    left: 0;
    width: 100%;
    margin: 0;
    text-align: center;
    font-family: "EB Garamond", serif;
    font-size: 24px;
    color: var(--author);
  }
  .cover-title-main {
    position: absolute;
    top: 315px;
    left: 0;
    width: 100%;
    margin: 0;
    text-align: center;
    font-family: "Montserrat", sans-serif;
    font-weight: 600;
    font-size: 108px;
    letter-spacing: 0.08em;
    text-indent: 0.08em;
    color: var(--teal);
    line-height: 1;
  }
  .cover-band {
    position: absolute;
    left: 0;
    top: 0;
    width: 540px;
    height: 790px;
  }
  .blurb-badge {
    position: absolute;
    left: 175px;
    top: 540px;
    width: 144px;
    height: 144px;
    border-radius: 50%;
    border: 24px solid var(--white);
    background: radial-gradient(circle at 45% 35%, #e8903a 0%, var(--amber) 60%, #b8621f 100%);
    display: flex;
    align-items: center;
    justify-content: center;
    box-sizing: content-box;
  }
  .blurb-text {
    margin: 0;
    width: 112px;
    text-align: center;
    font-family: "Oswald", sans-serif;
    font-size: 14px;
    line-height: 1.22;
    text-transform: uppercase;
    color: var(--white);
  }
</style>
</head>
<body>
<div class="canvas">
  <div class="cover">
    <svg class="cover-band" viewBox="0 0 540 790" aria-hidden="true">
      <defs>
        <linearGradient id="bandFill" x1="0" y1="0" x2="1" y2="0">
          <stop offset="0" stop-color="var(--orange)"/>
          <stop offset="1" stop-color="var(--orange-deep)"/>
        </linearGradient>
      </defs>
      <path d="M0,590 C120,470 390,420 540,555 L540,790 L0,790 Z" fill="url(#bandFill)"/>
    </svg>
    <h2 class="cover-title-top">THE</h2>
    <p class="cover-author">Marcus Pellworth</p>
    <h1 class="cover-title-main">PLEDGE</h1>
    <div class="blurb-badge">
      <p class="blurb-text">Get clarity, focus, and a new zest for life by following The Pledge for just 21 days</p>
    </div>
  </div>
</div>
</body>
</html>
```